Nordic Joinery Guild Wordpress Theme and newsletter template

We at the NJG are looking to start a Wordpress website and also send out a newsletter (web). We have just completed a Logo design project with ArtFlockly and we were so pleased with the results that we would like to see what the designers can come up with for a Wordpress theme and a template for an online newsletter. The theme has to support Icelandic letters. It also has to have a subscription option by email. We would need to have the option to add advertisement banners. The theme has to be easy to work with.
Below we have added a two websites for a example of what we are looking for: .
http://www.torvexhub.example/
http://www.brakkel.example/
The newsletter has to have a similar theme as the website and will be used with MS Publisher.

Attached is the new NJG logo.
Updates

Project Deadline Extended Reason: Not fully happy with the designs we have gotten so far. Would like to extend time to see if improvements can be made. Added Tuesday, June 16, 2015

Target Market(s)

Welding association members, welding and metalworking industry, suppliers in welding industry, International welding community, other national welding associations, welding education community

Industry/Entity Type

Welding

Number of Pages Required

3 page

Requirements
Must have
• The TKBÓ logo
• Icelandic letters
• email formpage
• Advertisement space/banners/buttons
• Easy to manage
• Compatible with Wordpress
Nice to have
• Welding pictures
• Nice graphics
Should not have
• Should not be dark and heavy set.

```html
<!DOCTYPE html>
<html lang="is">
<head>
<meta charset="utf-8">
<title>TKBÓ – Nordic Joinery Guild</title>
<link rel="stylesheet" href="https://fonts.googleapis.com/css2?family=Open+Sans:wght@300;400;600;700;800&display=swap">
<style>
:root{
  --red:#e8313a;
  --red-dark:#c9242c;
  --ink:#2a2a2a;
  --text:#555;
  --muted:#888;
  --line:#d6d6d6;
  --bar:#2e2e2e;
  --footer:#3b3b3b;
  --white:#fff;
}
*{box-sizing:border-box;margin:0;padding:0}
html,body{width:1200px;height:2390px;overflow:hidden}
body{font-family:"Open Sans",Arial,sans-serif;color:var(--text);background:var(--white);position:relative}
.wrap{position:absolute;left:99px;width:1002px}

/* header */
.site-header{position:absolute;left:0;top:0;width:1200px;height:105px;background:var(--white)}
.brand{position:absolute;left:99px;top:22px;display:flex;align-items:center;gap:8px}
.brand-dot{width:14px;height:14px;border-radius:50%;background:var(--red)}
.brand-name{font-weight:800;font-size:34px;color:var(--red);letter-spacing:-1px;line-height:1}
.brand-sub{position:absolute;left:99px;top:66px;font-size:8px;font-weight:700;color:var(--red);letter-spacing:.3px}
.contact{position:absolute;top:18px;display:flex;align-items:center;gap:8px;font-size:11.5px;color:#444;white-space:nowrap}
.contact .ico{flex:none;width:34px;height:34px;border-radius:50%;background:#ddd;display:flex;align-items:center;justify-content:center}
.contact.call{left:535px}
.contact.email{left:762px}
.lang{position:absolute;left:988px;top:17px;width:112px;height:34px;border:1px solid #ccc;border-radius:2px;font-size:10px;color:#666;display:flex;align-items:center;padding-left:10px;gap:6px;background:var(--white)}
.lang .flag{width:14px;height:9px;background:#2b3f8f}
.lang .caret{position:absolute;right:10px;top:12px}
.main-nav{position:absolute;top:72px;left:426px;width:675px;display:flex;justify-content:space-between;font-size:12.5px;font-weight:600;color:#333;text-transform:uppercase}

/* hero */
.hero{position:absolute;left:0;top:105px;width:1200px;height:466px;overflow:hidden}
.hero-photo{position:absolute;inset:0;background:linear-gradient(100deg,#4a3b33 0%,#1f2a55 45%,#2d4bb0 65%,#121831 100%)}
.hero-shape{position:absolute;inset:0}
.hero-copy{position:absolute;left:91px;top:134px;width:360px;color:var(--white)}
.hero-kicker{font-size:25px;font-weight:700;line-height:1.1}
.hero-title{font-size:29px;font-weight:300;line-height:1.2;margin-top:4px}
.hero-lead{font-size:14.5px;font-weight:700;line-height:1.65;margin-top:12px}
.hero-body{font-size:11px;line-height:1.95;margin-top:10px}
.btn-dark{display:inline-block;margin-top:30px;width:137px;height:40px;line-height:40px;text-align:center;background:#3a3a3a;color:var(--white);font-size:13px;font-weight:700;text-transform:uppercase;border-radius:2px}

/* tabs */
.sector-bar{position:absolute;left:0;top:571px;width:1200px;height:81px;background:var(--bar)}
.sector-tabs{position:absolute;left:99px;top:0;width:1002px;height:81px;display:flex}
.sector-tab{flex:1;padding:22px 0 0 35px;border-right:1px solid #444;color:var(--white)}
.sector-tab.active{background:var(--red);border-right:0}
.sector-tab h3{font-size:13px;font-weight:700;text-transform:uppercase}
.sector-tab p{font-size:9.5px;margin-top:6px;text-transform:uppercase;color:#ccc}
.sector-tab.active p{color:#fde}

/* ad banner */
.ad-banner{position:absolute;left:99px;top:680px;width:1002px;height:103px;background:linear-gradient(90deg,#5a2e1c,#2a1a14 40%,#1a1612);border:2px solid #111;display:flex;align-items:center;justify-content:center;gap:26px}
.ad-text{font-weight:800;color:var(--white);text-transform:uppercase;line-height:1.05}
.ad-text .l1{font-size:22px}
.ad-text .l1 b{color:var(--red);font-size:30px}
.ad-text .l2{font-size:22px}
.ad-text .l2 b{color:#f5a623;font-size:31px}
.ad-btn{border:2px solid #f5a623;color:#f5a623;font-size:12px;font-weight:700;padding:5px 14px;text-transform:uppercase;margin-top:26px}

/* welcome */
.section-title{font-size:22px;font-weight:700;color:var(--ink);text-align:center;text-transform:uppercase}
.welcome{top:818px}
.intro{font-size:11px;line-height:2;text-align:center;color:var(--muted);width:880px;margin:18px auto 0}

.features{top:984px;display:flex;justify-content:space-between}
.feature{width:314px}
.feature h3{font-size:16px;font-weight:700;color:var(--ink);text-transform:uppercase}
.feature .ph{width:314px;height:167px;margin-top:14px}
.feature h4{font-size:12px;font-weight:600;color:#333;line-height:1.9;text-transform:uppercase;margin-top:14px}
.feature p{font-size:11px;line-height:2.05;color:var(--muted);margin-top:10px}
.btn-red{display:inline-block;background:var(--red);color:var(--white);font-size:11px;font-weight:600;text-transform:uppercase;text-align:center;border-radius:2px}
.feature .btn-red{width:135px;height:37px;line-height:37px;margin-top:18px}

/* posts */
.posts{position:absolute;left:0;top:1452px;width:1200px;height:547px;background:linear-gradient(135deg,#3a3a3a,#1b1b1b 55%,#2a2a2a)}
.posts .section-title{color:var(--white);padding-top:58px}
.posts .intro{color:#ddd;font-size:12px;width:860px;margin-top:18px}
.post-grid{position:absolute;left:99px;top:188px;width:1002px;display:flex;justify-content:space-between}
.post{width:226px}
.post .ph{height:157px}
.post h4{font-size:11.5px;font-weight:700;color:var(--white);text-transform:uppercase;margin-top:16px}
.post time{display:block;font-size:11px;color:#ddd;margin-top:9px}
.posts .btn-red{position:absolute;left:500px;top:441px;width:199px;height:49px;line-height:49px;font-size:12.5px;font-weight:700}

/* newsletter */
.newsletter{top:2052px}
.signup{top:2122px;display:grid;grid-template-columns:323px 323px 324px;column-gap:15px;row-gap:21px}
.field{height:39px;border:1px solid var(--line);border-radius:2px;font-size:10.5px;color:#666;padding:0 16px;display:flex;align-items:center}
.signup .btn-red{width:194px;height:38px;line-height:38px;font-weight:700}

/* footer */
.site-footer{position:absolute;left:0;top:2285px;width:1200px;height:105px;background:var(--footer)}
.footer-brand{position:absolute;left:99px;top:33px;font-size:30px;font-weight:800;color:#888;letter-spacing:-1px}
.copyright{position:absolute;left:224px;top:46px;font-size:11px;color:#aaa}
.social{position:absolute;left:744px;top:36px;display:flex;align-items:center;gap:9px;font-size:11px;color:#aaa}
.social .dot{width:28px;height:28px;border-radius:50%;background:#5e5e5e}
.social span{margin-right:4px}
</style>
</head>
<body>

<header class="site-header">
  <div class="brand"><span class="brand-dot"></span><span class="brand-name">TKBÓ</span></div>
  <div class="brand-sub">TENGSLAFÉLAG KUNNÁTTU</div>

  <div class="contact call">
    <span class="ico"><svg width="14" height="11" viewBox="0 0 14 11"><rect x="0.5" y="0.5" width="13" height="10" fill="none" stroke="#666"/><path d="M1 1l6 5 6-5" fill="none" stroke="#666"/></svg></span>
    <span>CALL US : ( 4410 ) 552 318</span>
  </div>
  <div class="contact email">
    <span class="ico"><svg width="14" height="14" viewBox="0 0 24 24"><path d="M6.6 10.8a15.1 15.1 0 006.6 6.6l2.2-2.2a1 1 0 011-.25 11.4 11.4 0 003.6.57 1 1 0 011 1V20a1 1 0 01-1 1A17 17 0 013 4a1 1 0 011-1h3.5a1 1 0 011 1c0 1.25.2 2.45.57 3.6a1 1 0 01-.25 1z" fill="#666"/></svg></span>
    <span>EMAIL US : info@tkbo.example</span>
  </div>
  <div class="lang"><span class="flag"></span>ENGLISH
    <svg class="caret" width="8" height="6" viewBox="0 0 8 6"><path d="M1 1l3 3 3-3" fill="none" stroke="#777"/></svg>
  </div>

  <nav class="main-nav">
    <span>Home</span><span>About us</span><span>Services</span><span>Blog</span><span>Testimonials</span><span>Contact us</span>
  </nav>
</header>

<section class="hero">
  <div class="hero-photo" role="img" aria-label="Two welders in blue overalls and masks working with sparks flying"></div>
  <svg class="hero-shape" width="1200" height="466" viewBox="0 0 1200 466">
    <polygon points="0,0 420,0 625,466 0,466" fill="#e8313a" opacity="0.88"/>
    <polygon points="0,0 250,0 0,150" fill="#c9242c" opacity="0.55"/>
    <polygon points="420,0 470,0 625,466 560,466" fill="#ff5a60" opacity="0.35"/>
  </svg>
  <div class="hero-copy">
    <div class="hero-kicker">WE ARE A</div>
    <div class="hero-title">WELDING ASSOCIATION</div>
    <div class="hero-lead">Lorem Ipsum is simply dummy text of the printing and typesetting industry.</div>
    <div class="hero-body">Lorem Ipsum is simply dummy text of the printing and typesetting industry. Lorem Ipsum has been the industry's standard dummy text ever since the 1500s</div>
    <span class="btn-dark">Click here</span>
  </div>
</section>

<div class="sector-bar">
  <div class="sector-tabs">
    <div class="sector-tab active"><h3>Welding and metalworking industry</h3><p>Click here for view details &#187;</p></div>
    <div class="sector-tab"><h3>Suppliers in welding industry</h3><p>Click here for view details &#187;</p></div>
    <div class="sector-tab"><h3>International welding community</h3><p>Click here for view details &#187;</p></div>
  </div>
</div>

<aside class="ad-banner" aria-label="Advertisement banner">
  <div class="ad-text">
    <div class="l1">The <b>Targets</b> are</div>
    <div class="l2">Welding <b>Association Members</b></div>
  </div>
  <span class="ad-btn">Click here</span>
</aside>

<section class="wrap welcome">
  <h2 class="section-title">Welcome to TKBÓ</h2>
  <p class="intro">Lorem Ipsum is simply dummy text of the printing and typesetting industry. Lorem Ipsum has been the industry's standard dummy text ever since the 1500s, when an unknown printer took a galley of type and scrambled it to make a type specimen book. It has survived not only five centuries, but also the leap into electronic typesetting, remaining essentially unchanged.</p>
</section>

<section class="wrap features">
  <article class="feature">
    <h3>Find a course</h3>
    <div class="ph" role="img" aria-label="Smiling worker in a white hard hat with a team on a site" style="background:linear-gradient(135deg,#e8b04a,#d7dde4 55%,#9bb3c9)"></div>
    <h4>Lorem Ipsum is simply dummy text of the printing and typesetting industry</h4>
    <p>Lorem Ipsum is simply dummy text of the printing and typesetting industry. Lorem Ipsum has been the industry's standard dummy text ever since the 1500s...</p>
    <span class="btn-red">Read more info</span>
  </article>
  <article class="feature">
    <h3>Get certified</h3>
    <div class="ph" role="img" aria-label="Engineer in a yellow hard hat on the phone under a steel structure" style="background:linear-gradient(160deg,#2f6fb8,#7fb1e0 55%,#2a3550)"></div>
    <h4>Lorem Ipsum is simply dummy text of the printing and typesetting industry</h4>
    <p>Lorem Ipsum is simply dummy text of the printing and typesetting industry. Lorem Ipsum has been the industry's standard dummy text ever since the 1500s...</p>
    <span class="btn-red">Read more info</span>
  </article>
  <article class="feature">
    <h3>Careers in welding</h3>
    <div class="ph" role="img" aria-label="Welder in a mask with a bright welding flash" style="background:radial-gradient(circle at 35% 45%,#f4f6ff 0,#8da0c8 18%,#3d4a5e 45%,#6a4630 100%)"></div>
    <h4>Lorem Ipsum is simply dummy text of the printing and typesetting industry</h4>
    <p>Lorem Ipsum is simply dummy text of the printing and typesetting industry. Lorem Ipsum has been the industry's standard dummy text ever since the 1500s...</p>
    <span class="btn-red">Read more info</span>
  </article>
</section>

<section class="posts">
  <h2 class="section-title">Recent posts</h2>
  <p class="intro">Lorem Ipsum is simply dummy text of the printing and typesetting industry. Lorem Ipsum has been the industry's standard dummy text ever since the 1500s, when an unknown printer took a galley of type and scrambled</p>
  <div class="post-grid">
    <article class="post">
      <div class="ph" role="img" aria-label="Worker in an orange hard hat in a factory" style="background:linear-gradient(135deg,#6b7a85,#3b4248 50%,#b5522a)"></div>
      <h4>Lorem Ipsum is simply dummy</h4><time>Posted on 27 march 2015</time>
    </article>
    <article class="post">
      <div class="ph" role="img" aria-label="Grinding sparks in a dark workshop" style="background:radial-gradient(circle at 55% 60%,#ffe29a 0,#d08a2a 25%,#3a2a1c 70%)"></div>
      <h4>Lorem Ipsum is simply dummy</h4><time>Posted on 27 march 2015</time>
    </article>
    <article class="post">
      <div class="ph" role="img" aria-label="Hands cutting metal with sparks" style="background:linear-gradient(135deg,#c4652a,#e9a24b 45%,#4a3226)"></div>
      <h4>Lorem Ipsum is simply dummy</h4><time>Posted on 27 march 2015</time>
    </article>
    <article class="post">
      <div class="ph" role="img" aria-label="Welder in a protective mask at work" style="background:linear-gradient(135deg,#2a2c33,#6d5a52 50%,#8e95a8)"></div>
      <h4>Lorem Ipsum is simply dummy</h4><time>Posted on 27 march 2015</time>
    </article>
  </div>
  <span class="btn-red">View more posts</span>
</section>

<section class="wrap newsletter">
  <h2 class="section-title">Newsletter signup</h2>
</section>
<form class="wrap signup">
  <div class="field">Name :</div>
  <div class="field">Telephone :</div>
  <div class="field">Company worked for :</div>
  <div class="field">Personal ID number :</div>
  <div class="field">Email :</div>
  <span class="btn-red">Subscribe now</span>
</form>

<footer class="site-footer">
  <div class="footer-brand">TKBÓ</div>
  <div class="copyright">© Copyrights, 2015, TKBÓ. All rights reserved.</div>
  <div class="social">
    <span>Connect with our social network :</span>
    <i class="dot" aria-label="Social link"></i><i class="dot" aria-label="Social link"></i><i class="dot" aria-label="Social link"></i><i class="dot" aria-label="Social link"></i><i class="dot" aria-label="Social link"></i>
  </div>
</footer>

</body>
</html>
```